Modern, Sleek & Vibrant design required for electrical contracting work.

I require a flyer design for BRONVAL POWER SERVICES, which operates as an electrical contractor. We do electrical installations such as LED lighting, maintenance, repairs, communications and various other work related for residential and commercial customers. I would like the same colours applied from my logo to the flyer (Electric Blue, White, Grey/Silver). A6 or DL sizes with single side.

Target Market(s)

Residential and Commercial customers.

Industry/Entity Type

Communications

Font styles to use
Serif
Sans Serif

Requirements
Must have
• My logo and colours (Electric Blue, White, Silver/Grey)
Nice to have
• Shapes separating different parts of the flyer, such as the same electric bolt from my logo. Straight or angled shapes.
Should not have
• Childish pictures such as light bulbs. Curved shapes.

```html
<!DOCTYPE html>
<html lang="en">
<head>
<meta charset="utf-8">
<title>Bronval Power Services – Flyer</title>
<link href="https://fonts.googleapis.com/css2?family=Exo+2:wght@400;700;800&display=swap" rel="stylesheet">
<style>
  :root {
    --page-bg: #3a3a3c;
    --paper: #ffffff;
    --brand-blue: #2b3f9c;
    --brand-silver: #9ea3aa;
    --navy-deep: #0a1a2e;
    --btn-dark: #0f1522;
    --btn-navy: #0c2a4a;
    --btn-teal: #156b95;
    --text-light: #e4e7eb;
    --text-grey: #a7acb3;
  }
  * { box-sizing: border-box; margin: 0; padding: 0; }
  html, body {
    width: 880px; height: 1200px; overflow: hidden;
    background: var(--page-bg);
    font-family: "Exo 2", sans-serif;
  }
  .flyer {
    position: absolute; left: 199px; top: 173px;
    width: 493px; height: 693px;
    background: var(--paper);
    overflow: hidden;
    box-shadow: 0 6px 18px rgba(0,0,0,.45);
  }
  .flyer__hero {
    position: absolute; left: 0; top: 110px; width: 100%; height: 583px;
    background:
      radial-gradient(ellipse 70% 35% at 50% 28%, rgba(190,230,255,.55), transparent 70%),
      linear-gradient(180deg, #5aa9de 0%, #3f8fcb 28%, #2a6a9f 52%, #10263c 76%, #0b0f15 100%);
  }
  .flyer__divider { position: absolute; left: 0; top: 100px; width: 100%; height: 70px; }
  .brand {
    position: absolute; left: 0; top: 42px; width: 100%;
    display: flex; align-items: center; justify-content: center; gap: 12px;
  }
  .brand__dot {
    width: 34px; height: 34px; border-radius: 50%;
    background: var(--brand-silver);
  }
  .brand__name {
    font-weight: 800; font-size: 27px; letter-spacing: .5px;
    color: var(--brand-blue);
  }
  .services {
    position: absolute; left: 113px; top: 206px; width: 267px;
    list-style: none;
  }
  .services__item {
    height: 43px; margin-bottom: 13.5px;
    display: flex; align-items: center; justify-content: center;
    color: #fff; font-weight: 800; font-size: 20px; letter-spacing: .3px;
    box-shadow: 3px 4px 8px rgba(0,0,0,.45);
  }
  .services__item--dark { background: var(--btn-dark); }
  .services__item--navy { background: var(--btn-navy); }
  .services__item--teal { background: var(--btn-teal); }
  .services__item:last-child { margin-top: 16px; }
  .contact {
    position: absolute; left: 0; top: 582px; width: 100%; text-align: center;
  }
  .contact__name { font-weight: 700; font-size: 22px; color: var(--text-grey); line-height: 1.1; }
  .contact__role { font-size: 15px; color: var(--text-grey); line-height: 1; }
  .contact__email {
    margin-top: 22px;
    display: flex; align-items: center; justify-content: center; gap: 9px;
    font-size: 17px; color: var(--text-light);
  }
  .contact__icon { width: 24px; height: 16px; }
</style>
</head>
<body>
  <main class="flyer">
    <div class="flyer__hero" role="img" aria-label="Blurred blue background of glowing LED stadium lights"></div>
    <svg class="flyer__divider" viewBox="0 0 493 70" preserveAspectRatio="none" aria-hidden="true">
      <polygon points="0,0 493,0 493,12 0,38" fill="var(--paper)"/>
      <polygon points="0,38 493,12 493,16 0,42" fill="var(--brand-silver)"/>
      <polygon points="0,42 493,16 493,34 0,60" fill="var(--navy-deep)"/>
    </svg>

    <header class="brand">
      <span class="brand__dot"></span>
      <span class="brand__name">BRONVAL POWER SERVICES</span>
    </header>

    <ul class="services">
      <li class="services__item services__item--dark">LED LIGHTING</li>
      <li class="services__item services__item--dark">INSTALLATIONS</li>
      <li class="services__item services__item--navy">MAINTENANCE</li>
      <li class="services__item services__item--navy">REPAIRS</li>
      <li class="services__item services__item--teal">COMMUNICATIONS</li>
      <li class="services__item services__item--teal">EMERGENCY CALL-OUTS</li>
    </ul>

    <footer class="contact">
      <p class="contact__name">Dario Venlo</p>
      <p class="contact__role">Director</p>
      <p class="contact__email">
        <svg class="contact__icon" viewBox="0 0 24 16" aria-hidden="true">
          <rect x="0.5" y="0.5" width="23" height="15" fill="#3f56c4" stroke="#6f84e6"/>
          <path d="M1 1 L12 9 L23 1" fill="none" stroke="#c9d3ff" stroke-width="1.4"/>
        </svg>
        dario@bronvalpower.com
      </p>
    </footer>
  </main>
</body>
</html>
```